CD Cover and case - 8 page booklet

BUDGET NEGOTIABLE. Should I find a design which I really love then I am willing to increase the budget. I am looking for a quote for a CD case and disc to be created for my upcoming Welsh language album. Initially looking for a demo of possible front cover, then I will discuss booklet/disc design and budget with chosen designer. CD will be a jewel case with clear tray and 8 page booklet. Previous experience of CD cover design and demos essential. Title of CD is 'Rhodri Penlan - Golau'r Ffin'. Album is Pop/Rock/Ballads style. Either of the pictures attached could be used as a front cover. The project is due to be released in August so no major hurry, once I have decided which design/designer to use I will start work on the sleeve notes and should hopefully have them ready within a month. Many Thanks
Target Market(s)
Wide age range from 20s to 50s target audience.
Industry/Entity Type
Music Download
Look and feel
Each slider illustrates characteristics of the customer's brand and the style your logo design should communicate.

```html
<!DOCTYPE html>
<html lang="cy">
<head>
<meta charset="utf-8">
<title>Rhodri Penlan – Golau'r Ffin</title>
<link rel="stylesheet" href="https://fonts.googleapis.com/css2?family=Josefin+Sans:wght@600&family=Jost:wght@400&display=swap">
<style>
  :root {
    --ink: #0a0a0a;
    --paper: #f2f2f2;
    --stone-light: #d9d9d9;
    --stone-mid: #9a9a9a;
    --stone-dark: #3c3c3c;
    --jacket: #2e2e2e;
    --portrait-top: #5d6b66;
    --portrait-skin: #b57a5e;
    --portrait-navy: #1f2a44;
    --name-light: #ffffff;
    --name-shade: #9c9c9c;
  }
  html, body {
    margin: 0;
    padding: 0;
    overflow: hidden;
    background: var(--paper);
  }
  .cover {
    position: relative;
    width: 1200px;
    height: 1200px;
    overflow: hidden;
    background: var(--paper);
  }
  .backdrop-photo {
    position: absolute;
    inset: 0;
    background:
      radial-gradient(ellipse 420px 520px at 840px 1060px, var(--jacket) 0%, var(--jacket) 55%, rgba(46,46,46,0) 75%),
      linear-gradient(90deg, var(--stone-light) 0%, var(--stone-mid) 18%, var(--stone-dark) 30%, var(--stone-mid) 48%, var(--stone-light) 62%, var(--stone-mid) 100%);
    filter: blur(2px);
  }
  .portrait-photo {
    position: absolute;
    left: 574px;
    top: 59px;
    width: 560px;
    height: 654px;
    background:
      radial-gradient(ellipse 190px 240px at 330px 300px, var(--portrait-skin) 0%, var(--portrait-skin) 60%, rgba(181,122,94,0) 100%),
      linear-gradient(180deg, var(--portrait-top) 0%, #4a524f 60%, var(--portrait-navy) 100%);
    box-shadow: 0 14px 24px rgba(0,0,0,0.45);
  }
  .name-block {
    position: absolute;
    left: 50px;
    top: 182px;
    width: 525px;
    height: 418px;
    background: var(--ink);
  }
  .artist-name {
    position: absolute;
    left: 32px;
    top: 108px;
    margin: 0;
    font-family: "Josefin Sans", sans-serif;
    font-weight: 600;
    font-size: 86px;
    line-height: 92px;
    letter-spacing: 0.07em;
    text-transform: uppercase;
    background: linear-gradient(100deg, var(--name-light) 0%, var(--name-shade) 40%, var(--name-light) 70%, var(--name-shade) 100%);
    -webkit-background-clip: text;
    background-clip: text;
    color: transparent;
  }
  .cross-mark {
    position: absolute;
    left: 236px;
    top: 704px;
    width: 122px;
    height: 122px;
  }
  .album-title {
    position: absolute;
    left: 46px;
    top: 920px;
    margin: 0;
    font-family: "Jost", sans-serif;
    font-weight: 400;
    font-size: 128px;
    line-height: 150px;
    color: var(--ink);
    letter-spacing: 0.02em;
    white-space: nowrap;
  }
</style>
</head>
<body>
  <main class="cover">
    <div class="backdrop-photo" role="img" aria-label="Black and white photo of the singer in a dark blazer and printed T-shirt standing in front of an old stone building"></div>
    <div class="portrait-photo" role="img" aria-label="Colour close-up portrait of the singer wearing glasses, looking up and to the side"></div>

    <div class="name-block">
      <h1 class="artist-name">Rhodri<br>Penlan</h1>
    </div>

    <svg class="cross-mark" viewBox="0 0 100 100" aria-hidden="true">
      <path d="M14 4 L50 40 L86 4 L96 14 L60 50 L96 86 L86 96 L50 60 L14 96 L4 86 L40 50 L4 14 Z" fill="var(--ink)"/>
    </svg>

    <h2 class="album-title">Golau'r Ffin</h2>
  </main>
</body>
</html>
```